VarnLink Signal Systems Website Design

We are an Australian based telecommunications company who specialise in the design, build and implementation of mission critical communications infrastructure. We have offices throughout Australia, New Zealand and Europe. Our Customers are operators in multiple markets from Oil & Gas, Mining, Government, Utilities, Carrier & Transportation.

We also work with large multi-national companies, that provide telecommunication and services such as; Pelvaro, Dransvik, Quorba, Talmoss and many more. We want to be able to achieve the same level of impressions and professionalism as what these companies present on their websites.

To reflect our recent move into the European market, we need our new site to reflect who we are as a company, and exhibit the fact we are not just based in Australia, but we are a global organisation. We want to have a fresh clean look, thats modern, dynamic and simple. Flat textures and colours are perfect for us to adapt to. A site that is based around content management, with a responsive design that can be used on all devices.

We have started to develop a basic design language that we would like to incorporate in our overall website design. We have attached some documents that highlight our design language and we can provide colour codes and fonts to ensure consistency.

Our existing site is: www.varnlinkss.example. Please feel free to view and pick apart items. From this example, we would massive improvement in how the site looks, feels and functions. We also want social media to form a big part of our site, with the likes of posts from chirpnet and blogs posting capabilities.

If you require anymore information about VarnLink or our requirements, please do not hesitate to contact.

Thanks and good luck!

Target Market(s)

Potential & Existing Customers, New international customers & markets, New Market Sectors, Partners, Service Providers

Industry/Entity Type

Telecommunications

Coding

Coded - Design and coding required

Number of Pages Required

5+ page

Font styles to use
Sans Serif

Requirements
Must have
• Content Management, Responsive Design for multiple device compatibility, Social media integration, use of lots of imagery, drop down menus, search capabilities
Should not have
• No flash.

```html
<!DOCTYPE html>
<html lang="en">
<head>
<meta charset="utf-8">
<title>VarnLink Signal Systems</title>
<link rel="stylesheet" href="https://fonts.googleapis.com/css2?family=Open+Sans:wght@400;600&family=Roboto+Condensed:wght@300;400;700&display=swap">
<style>
:root{
  --navy:#1d3461;
  --navy-deep:#17294d;
  --violet:#8d87c2;
  --ink:#3a3a3a;
  --muted:#6b6b6b;
  --grey-band:#f1f1f1;
  --white:#ffffff;
  --head:"Roboto Condensed",Arial,sans-serif;
  --body:"Open Sans",Arial,sans-serif;
}
*{box-sizing:border-box;margin:0;padding:0}
html,body{width:1200px;height:2871px;overflow:hidden}
body{position:relative;background:var(--white);font-family:var(--body);color:var(--ink)}
.abs{position:absolute}

/* top bar */
.topbar{left:0;top:0;width:1200px;height:42px;background:var(--navy)}
.topbar .search{left:455px;top:0;width:300px;height:42px;display:flex;align-items:center;justify-content:space-between;color:#fff;font-family:var(--head);font-size:18px}
.topbar .phone{left:950px;top:0;height:42px;display:flex;align-items:center;gap:10px;color:#fff;font-family:var(--head);font-size:19px}

/* header */
.header{left:0;top:42px;width:1200px;height:92px;background:#fff}
.brand{left:76px;top:16px;color:var(--navy);font-family:var(--head);font-weight:700;line-height:1}
.brand .name{font-size:40px;letter-spacing:.5px}
.brand .sub{font-size:11px;letter-spacing:1.5px;margin-top:4px;padding-left:110px}
.nav{left:398px;top:38px;display:flex;gap:0;font-family:var(--head);font-size:17px;color:#555}
.nav a{color:inherit;text-decoration:none;position:absolute;white-space:nowrap}
.nav a.active{color:var(--navy)}

/* hero */
.hero{left:0;top:134px;width:1200px;height:574px;background:linear-gradient(180deg,#d9dcdf 0%,#c4c8cc 45%,#8d949a 75%,#3e4247 100%)}
.hero-caption{left:404px;top:374px;width:796px;height:150px;background:rgba(29,52,97,.55);padding:10px 52px 0 0;text-align:right;color:#fff;font-family:var(--head);font-size:35px;line-height:1.07;font-weight:400}

/* welcome */
.section-title{width:1200px;left:0;text-align:center;font-family:var(--head);font-size:46px;font-weight:400;color:#555}
.section-title b{color:var(--navy);font-weight:400}
.welcome-title{top:752px}
.lead{left:148px;width:904px;text-align:center;font-size:15px;line-height:1.55;color:var(--muted)}
.welcome-lead{top:822px}
.service{top:962px;width:200px;text-align:center}
.service svg{display:block;margin:0 auto}
.service h3{font-family:var(--head);font-weight:400;font-size:20px;color:var(--navy);line-height:1.5;margin-top:10px}
.service p{font-size:14px;line-height:1.65;color:var(--muted);margin-top:6px;padding:0 22px}

/* sectors */
.sectors{left:0;top:1332px;width:1200px;height:416px;background:var(--grey-band)}
.sectors-title{top:1382px}
.sectors-lead{top:1450px}
.sector{top:1514px;width:188px}
.sector .shot{width:188px;height:124px}
.sector span{display:block;text-align:center;margin-top:20px;font-family:var(--head);font-size:20px;color:var(--navy-deep)}

/* support */
.support{left:0;top:1748px;width:1200px;height:520px;background:linear-gradient(90deg,#f7f7f8 0%,#eceef1 38%,#b9c6d8 62%,#e6e6e6 85%,#d8d9dc 100%)}
.support h2{left:80px;top:1820px;font-family:var(--head);font-weight:300;font-size:58px;color:#444}
.support h2 b{color:var(--navy);font-weight:400}
.support-text{left:80px;top:1900px;width:560px;font-size:21px;line-height:1.75;color:#333}
.btn{left:77px;top:2084px;width:200px;height:58px;border-radius:29px;background:var(--navy);color:#fff;font-family:var(--head);font-size:19px;display:flex;align-items:center;padding-left:24px}
.btn .arrow{position:absolute;right:0;top:0;width:58px;height:58px;border-radius:50%;background:var(--navy);border:3px solid #fff;display:flex;align-items:center;justify-content:center}

/* partners */
.partners-title{top:2310px;color:#555}
.partner{top:2392px;width:220px;height:50px;display:flex;align-items:center;justify-content:center;font-family:var(--head);font-weight:700;font-size:32px;color:#2b2b2b}

/* footer */
.footer{left:0;top:2507px;width:1200px;height:310px;background:var(--navy)}
.fcol{top:2544px;color:#fff}
.fcol h4{font-family:var(--head);font-weight:400;font-size:22px;margin-bottom:12px}
.fcol li{list-style:none;font-size:15px;line-height:26px}
.fbrand{left:890px;top:2540px;width:230px;color:#fff}
.fbrand .name{font-family:var(--head);font-weight:700;font-size:34px;text-align:center}
.fbrand .sub{font-family:var(--head);font-weight:700;font-size:10px;letter-spacing:1.5px;text-align:center;margin-top:2px}
.fbrand p{font-size:15px;line-height:1.7;margin-top:30px}
.bottombar{left:0;top:2817px;width:1200px;height:54px;background:var(--navy-deep);color:#fff;font-size:15px;display:flex;align-items:center;padding-left:80px}
.social{right:70px;top:2833px;display:flex;gap:22px}
.social span{width:20px;height:20px;border-radius:50%;background:#fff;display:block}
</style>
</head>
<body>

<div class="abs topbar">
  <div class="abs search"><span>Search here...</span>
    <svg width="20" height="20" viewBox="0 0 20 20"><circle cx="8" cy="8" r="6" fill="none" stroke="#fff" stroke-width="2.6"/><line x1="12.5" y1="12.5" x2="18" y2="18" stroke="#fff" stroke-width="3" stroke-linecap="round"/></svg>
  </div>
  <div class="abs phone">
    <svg width="20" height="20" viewBox="0 0 24 24"><path fill="#fff" d="M6.6 10.8a15.1 15.1 0 0 0 6.6 6.6l2.2-2.2c.3-.3.7-.4 1-.2 1.1.4 2.3.6 3.6.6.6 0 1 .4 1 1V20c0 .6-.4 1-1 1A17 17 0 0 1 3 4c0-.6.4-1 1-1h3.5c.6 0 1 .4 1 1 0 1.3.2 2.5.6 3.6.1.3 0 .7-.2 1z"/></svg>
    <span>+61 3 5550 0142</span>
  </div>
</div>

<header class="abs header">
  <div class="abs brand"><div class="name">VarnLink</div><div class="sub">SIGNAL SYSTEMS</div></div>
  <nav class="abs nav">
    <a class="active" style="left:0">HOME</a>
    <a style="left:90px">PRODUCT &amp; SERVICES</a>
    <a style="left:293px">SECTORS</a>
    <a style="left:404px">SUPPORT</a>
    <a style="left:517px">CORPORATE</a>
    <a style="left:651px">CONTACT</a>
  </nav>
</header>

<section class="abs hero" role="img" aria-label="Open-plan office with staff working at desks beneath a tree wall mural"></section>
<div class="abs hero-caption">To be a leading international provider of advanced and engineered solutions for mission and business critical network</div>

<h1 class="abs section-title welcome-title">Welcome to <b>VarnLink Signal Systems</b></h1>
<p class="abs lead welcome-lead">VarnLink Signal Systems is an Australian owned company that provides turnkey communications networks to customers around the world. Founded in 1998, the company has grown to be the leading supplier of communications systems and equipment in its field. Our core business covers the utilities and carrier markets, and have succeeded in expanding our profile into the emergency services sector.</p>

<div class="abs service" style="left:72px">
  <svg width="130" height="130" viewBox="0 0 130 130"><path d="M115 65A50 50 0 1 1 65 15" fill="none" stroke="var(--violet)" stroke-width="3"/><path d="M65 15A50 50 0 0 1 115 65" fill="none" stroke="#d9d6ec" stroke-width="3"/><circle cx="115" cy="65" r="6" fill="var(--violet)"/>
  <g fill="none" stroke="var(--navy)" stroke-width="3" stroke-linejoin="round"><path d="M44 70h42v10H44z"/><path d="M52 70l13-16 13 16"/><path d="M58 58l7-8 7 8"/></g></svg>
  <h3>Supply &amp; Solution Development</h3>
  <p>The Supply &amp; Solutions developement team is responsible for the assessment...</p>
</div>
<div class="abs service" style="left:286px">
  <svg width="130" height="130" viewBox="0 0 130 130"><path d="M115 65A50 50 0 1 1 65 15" fill="none" stroke="var(--violet)" stroke-width="3"/><path d="M65 15A50 50 0 0 1 115 65" fill="none" stroke="#d9d6ec" stroke-width="3"/><circle cx="115" cy="65" r="6" fill="var(--violet)"/>
  <g fill="none" stroke="var(--navy)" stroke-width="3" stroke-linecap="round"><circle cx="65" cy="52" r="4"/><path d="M57 44a11 11 0 0 0 0 16M73 44a11 11 0 0 1 0 16M51 38a19 19 0 0 0 0 28M79 38a19 19 0 0 1 0 28"/><path d="M65 56l-9 28M65 56l9 28M59 74h12"/></g></svg>
  <h3>Rapid Site Solution</h3>
  <p>The Rapid Site Solution(RSS) team provides a unique semi-permanent, self-contained communications hut</p>
</div>
<div class="abs service" style="left:500px">
  <svg width="130" height="130" viewBox="0 0 130 130"><path d="M115 65A50 50 0 1 1 65 15" fill="none" stroke="var(--violet)" stroke-width="3"/><path d="M65 15A50 50 0 0 1 115 65" fill="none" stroke="#d9d6ec" stroke-width="3"/><circle cx="115" cy="65" r="6" fill="var(--violet)"/>
  <g fill="none" stroke="var(--navy)" stroke-width="3"><rect x="45" y="43" width="40" height="40" rx="6"/><path d="M52 54h26M52 63h26M52 72h26"/><circle cx="60" cy="54" r="3" fill="#fff"/><circle cx="70" cy="63" r="3" fill="#fff"/><circle cx="58" cy="72" r="3" fill="#fff"/></g></svg>
  <h3>Operational Support Systems</h3>
  <p>The Operational Support Systems (OSS) team is a specialist unit focusing on the development...</p>
</div>
<div class="abs service" style="left:714px">
  <svg width="130" height="130" viewBox="0 0 130 130"><path d="M115 65A50 50 0 1 1 65 15" fill="none" stroke="var(--violet)" stroke-width="3"/><path d="M65 15A50 50 0 0 1 115 65" fill="none" stroke="#d9d6ec" stroke-width="3"/><circle cx="115" cy="65" r="6" fill="var(--violet)"/>
  <g fill="none" stroke="var(--navy)" stroke-width="3" stroke-linecap="round"><path d="M47 64a18 18 0 0 1 36 0"/><rect x="43" y="60" width="7" height="13" rx="3"/><rect x="80" y="60" width="7" height="13" rx="3"/><path d="M83 73c0 8-6 11-14 11"/><path d="M50 88c4-5 26-5 30 0"/></g></svg>
  <h3>After Sales Support</h3>
  <p>The After Sales Support team offers flexible multi-technology and multi-vendors support services.</p>
</div>
<div class="abs service" style="left:928px">
  <svg width="130" height="130" viewBox="0 0 130 130"><path d="M115 65A50 50 0 1 1 65 15" fill="none" stroke="var(--violet)" stroke-width="3"/><path d="M65 15A50 50 0 0 1 115 65" fill="none" stroke="#d9d6ec" stroke-width="3"/><circle cx="115" cy="65" r="6" fill="var(--violet)"/>
  <g fill="none" stroke="var(--navy)" stroke-width="3" stroke-linejoin="round"><rect x="52" y="42" width="34" height="24"/><circle cx="50" cy="54" r="5"/><path d="M44 64h12v22M50 86v-12M64 60l8-6"/></g></svg>
  <h3>Training</h3>
  <p>The Training team provides and delivers an exctensive portfolio of technology, product and systems training courses</p>
</div>

<section class="abs sectors"></section>
<h2 class="abs section-title sectors-title">Our Business <b>Sectors</b></h2>
<p class="abs lead sectors-lead">VarnLink specialises in design and development of systems and networks that meet the stringent requirements of mission-critical industries.</p>
<div class="abs sector" style="left:77px"><div class="shot" role="img" aria-label="Gas processing plant with tanks under blue sky" style="background:linear-gradient(180deg,#4d88c9,#9fb6c9 55%,#7b7f6e)"></div><span>Oil &amp; Gas</span></div>
<div class="abs sector" style="left:291px"><div class="shot" role="img" aria-label="Electrical substation equipment" style="background:linear-gradient(180deg,#6d8fb5,#8a8c86 55%,#4d4a3f)"></div><span>Electricity Utilities</span></div>
<div class="abs sector" style="left:505px"><div class="shot" role="img" aria-label="Freight locomotive at sunset" style="background:linear-gradient(180deg,#e3a24b,#c8782e 55%,#3b2c1d)"></div><span>Transport</span></div>
<div class="abs sector" style="left:720px"><div class="shot" role="img" aria-label="Haul truck at an open-cut mine" style="background:linear-gradient(180deg,#9fb4cc,#b08a62 55%,#7a5a3c)"></div><span>Mining</span></div>
<div class="abs sector" style="left:934px"><div class="shot" role="img" aria-label="Telecommunications tower against blue sky" style="background:linear-gradient(180deg,#1e5fb0,#3f7ccb 60%,#2a5b9c)"></div><span>Carrier</span></div>

<section class="abs support" role="img" aria-label="Smiling support agent wearing a headset with colleagues behind"></section>
<h2 class="abs support" style="background:none;height:auto;width:auto" aria-hidden="false"></h2>
<h2 class="abs" style="left:80px;top:1820px;font-family:var(--head);font-weight:300;font-size:58px;color:#444">Technical <b style="color:var(--navy);font-weight:400">Support</b></h2>
<p class="abs support-text">VarnLink offers flexible, multi-technology and multi-vendor support services. We take an end-to-end view of networks, helping you to resolve issues quickly and completely.</p>
<a class="abs btn">READ MORE
  <span class="arrow"><svg width="24" height="20" viewBox="0 0 24 20"><path d="M3 3l7 7-7 7M12 3l7 7-7 7" fill="none" stroke="#fff" stroke-width="3"/></svg></span>
</a>

<h2 class="abs section-title partners-title">Our <b>Partner</b></h2>
<div class="abs partner" style="left:76px">Brevane</div>
<div class="abs partner" style="left:358px">Omlira</div>
<div class="abs partner" style="left:572px">Quorba</div>
<div class="abs partner" style="left:780px">Skelwater</div>
<div class="abs partner" style="left:960px">Dransvik</div>

<footer class="abs footer"></footer>
<div class="abs fcol" style="left:80px"><h4>Company</h4><ul><li>Home</li><li>About</li><li>Legal Information</li><li>Privacy Policy</li><li>Terms of Use</li><li>Cookies</li><li>Contact</li></ul></div>
<div class="abs fcol" style="left:350px"><h4>Business Services</h4><ul><li>Supply &amp; Solution Development</li><li>Rapid Site Solution</li><li>Operational Support Systems</li><li>After Sales Support</li><li>Professional Services</li><li>Training</li></ul></div>
<div class="abs fcol" style="left:622px"><h4>Business Sector</h4><ul><li>Oil &amp; Gas</li><li>Electricity Utilities</li><li>Transport</li><li>Mining</li><li>Carrier</li><li>Emergency Services</li></ul></div>
<div class="abs fbrand"><div class="name">VarnLink</div><div class="sub">SIGNAL SYSTEMS</div>
  <p>VarnLink Signal Systems is an Australian owned company providing turnkey communications networks, both within Australia and internationally.</p></div>

<div class="abs bottombar">© VarnLink Signal Systems - 2016. All Rights Reserved.</div>
<div class="abs social" aria-label="Social links"><span></span><span></span><span></span><span></span></div>

</body>
</html>
```